Telvor Enterprises has 5 divisions in the organisation.
One of them is our Soaps, Candles and Cosmetics range.

Our Logo is a ORVALE with the word ORVALE an image of a crown.
Orvale Supplements & Orvale Sports are 2 divisions.

Now we need to introduce our ORVALE COLLECTIONS which will include cosmetic, candles, fragrances etc.

What we need designed is an elegant, sophisticated label of our CANDLE JARS and Outer Box.

The same will flow through to our soaps and other collection.

This will the beginning of a long term relationship for the designer to maintain and update our Orvale Collections artwork.

Hello designers,

We have increases our 1st prize budget to $200.00

Please read the brief carefully.
We need this job wrapped up quickly.

It is a fairly simple project with huge long term potential.

We look forward to receiving some designs.

Reason: Due to the Easter Break last week, many people were off work. Therefore we have extended our deadline to allow other participants to submit their designs.

Reason: We have not found a design we like yet.

Industry/Entity Type

Cosmetics

Requirements
Must have
• The ORVALE and the word ORVALE must remain the same.
The word collections must be added under the crown.
The word collections to be Elegant, maybe cursive, or hand written.

Wording for Jar Label:
100% Soy Wax
Quality Essential oils & Fragrances
Hand made in Australia

Box Wording:
will be provided at later stage.
Make a mockup of a box but not too loud.
Sophisticated and elegant.
Do not use existing artwork from others.

Nice to have
• Special design label.

The width of the label to be no more than 50mm.
The height of the label to be no more than 60mm

We believe that the JAR label needs to be small and effective.
We beleive the box should use Royal colours and not too many flowers and vines. Elegance.
Should not have
• Should not be noisy, loud and full of information.

```html
<!DOCTYPE html>
<html lang="en">
<head>
<meta charset="utf-8">
<title>Orvale Collections – Box and Jar Label</title>
<link rel="stylesheet" href="https://fonts.googleapis.com/css2?family=Cinzel:wght@400&family=Cormorant+Garamond:ital,wght@0,400;1,400&display=swap">
<style>
  :root {
    --backdrop: #e9e6da;
    --box-white: #ffffff;
    --royal-gold: #a8940f;
    --gold-deep: #9a8608;
    --ivory-text: #f4f0df;
    --label-cream: #fbf8e4;
    --label-panel: #f6f4e6;
    --soft-gold: #c2ad6e;
    --warm-grey: #8f8f86;
    --ink: #1c1c1c;
  }
  * { margin: 0; padding: 0; box-sizing: border-box; }
  html, body { width: 1200px; height: 1000px; overflow: hidden; }
  body { background: var(--backdrop); position: relative; font-family: "Cinzel", serif; }

  /* ---------- Outer box, front face ---------- */
  .box-front {
    position: absolute; left: 70px; top: 60px; width: 470px; height: 860px;
    background: var(--box-white);
    box-shadow: 0 2px 10px rgba(0,0,0,0.08);
  }
  .box-front svg.box-frames { position: absolute; inset: 0; }
  .box-brand {
    position: absolute; left: 40px; width: 390px; text-align: center;
    color: var(--ivory-text); font-family: "Cinzel", serif; font-weight: 400;
  }
  .box-brand--name { top: 172px; font-size: 62px; letter-spacing: 1px; }
  .box-brand--range { top: 272px; font-size: 36px; letter-spacing: 1px; }
  .box-flourish-small {
    position: absolute; left: 175px; top: 330px; width: 120px; height: 36px;
    background: radial-gradient(ellipse at center, rgba(244,240,223,0.55), rgba(244,240,223,0) 70%);
  }
  .box-flourish-large {
    position: absolute; left: 115px; top: 425px; width: 240px; height: 240px;
    background: radial-gradient(ellipse at center, rgba(168,148,15,0.32), rgba(168,148,15,0.05) 70%, rgba(168,148,15,0) 75%);
  }
  .product-band {
    position: absolute; left: 80px; top: 512px; width: 310px; height: 72px;
    background: var(--box-white); border: 4px solid var(--royal-gold);
    display: flex; align-items: center; justify-content: center;
    font-family: "Cormorant Garamond", serif; font-size: 28px; color: var(--ink);
    letter-spacing: 0.5px;
  }
  .box-tagline {
    position: absolute; left: 0; width: 470px; top: 705px; text-align: center;
    font-family: "Cormorant Garamond", serif; font-size: 20px; line-height: 1.25;
    color: var(--royal-gold); letter-spacing: 0.5px;
  }

  /* ---------- Candle jar label ---------- */
  .jar-label {
    position: absolute; left: 630px; top: 190px; width: 440px; height: 620px;
    background: var(--label-cream);
    box-shadow: 0 2px 10px rgba(0,0,0,0.06);
  }
  .jar-label svg.label-frame { position: absolute; inset: 0; }
  .label-text { position: absolute; left: 0; width: 440px; text-align: center; }
  .label-brand { top: 168px; font-family: "Cinzel", serif; font-size: 54px; color: var(--soft-gold); letter-spacing: 1px; }
  .label-range { top: 266px; font-family: "Cinzel", serif; font-size: 33px; color: var(--warm-grey); letter-spacing: 1px; }
  .label-flourish {
    position: absolute; left: 175px; top: 318px; width: 90px; height: 30px;
    background: radial-gradient(ellipse at center, rgba(194,173,110,0.5), rgba(194,173,110,0) 70%);
  }
  .label-promise {
    top: 395px; font-family: "Cormorant Garamond", serif; font-style: italic;
    font-size: 22px; line-height: 1.3; color: var(--warm-grey);
  }
  .label-origin {
    top: 512px; font-family: "Cormorant Garamond", serif; font-style: italic;
    font-size: 18px; line-height: 1.3; color: var(--warm-grey);
  }
</style>
</head>
<body>

<section class="box-front" aria-label="Outer box front">
  <svg class="box-frames" width="470" height="860" viewBox="0 0 470 860" aria-hidden="true">
    <!-- outer hairline around the gold panel -->
    <path d="M50,50 H420 A20 20 0 0 0 440 70 V390 A20 20 0 0 0 420 410 H50 A20 20 0 0 0 30 390 V70 A20 20 0 0 0 50 50 Z"
          fill="none" stroke="var(--royal-gold)" stroke-width="3"/>
    <!-- gold panel -->
    <path d="M58,60 H412 A18 18 0 0 0 430 78 V382 A18 18 0 0 0 412 400 H58 A18 18 0 0 0 40 382 V78 A18 18 0 0 0 58 60 Z"
          fill="var(--royal-gold)"/>
    <!-- inner ivory rule -->
    <path d="M66,70 H404 A14 14 0 0 0 420 86 V374 A14 14 0 0 0 404 390 H66 A14 14 0 0 0 50 374 V86 A14 14 0 0 0 66 70 Z"
          fill="none" stroke="var(--ivory-text)" stroke-width="2"/>
    <!-- dividers -->
    <line x1="105" y1="162" x2="365" y2="162" stroke="var(--ivory-text)" stroke-width="1.5"/>
    <line x1="125" y1="255" x2="345" y2="255" stroke="var(--ivory-text)" stroke-width="1.5"/>
    <circle cx="235" cy="255" r="4" fill="var(--ivory-text)"/>
    <circle cx="224" cy="255" r="2.5" fill="var(--ivory-text)"/>
    <circle cx="246" cy="255" r="2.5" fill="var(--ivory-text)"/>
  </svg>
  <div class="box-brand box-brand--name">ORVALE</div>
  <div class="box-brand box-brand--range">COLLECTIONS</div>
  <div class="box-flourish-small" role="img" aria-label="Small calligraphic flourish"></div>
  <div class="box-flourish-large" role="img" aria-label="Ornamental gold scroll flourish behind the product name"></div>
  <div class="product-band">PRODUCT NAME</div>
  <p class="box-tagline">ESSENTIAL OILS &amp; FRAGRANCES<br>HAND MADE IN AUSTRALIA</p>
</section>

<section class="jar-label" aria-label="Candle jar label">
  <svg class="label-frame" width="440" height="620" viewBox="0 0 440 620" aria-hidden="true">
    <!-- arched panel with gold border -->
    <path d="M60,110 Q60,80 90,75 Q220,45 350,75 Q380,80 380,110 V430 Q380,460 350,470 Q220,500 90,470 Q60,460 60,430 Z"
          fill="var(--label-panel)" stroke="var(--soft-gold)" stroke-width="10"/>
    <path d="M76,118 Q76,94 100,90 Q220,64 340,90 Q364,94 364,118 V424 Q364,448 340,456 Q220,482 100,456 Q76,448 76,424 Z"
          fill="none" stroke="var(--soft-gold)" stroke-width="1.5"/>
    <!-- dividers -->
    <line x1="110" y1="155" x2="330" y2="155" stroke="var(--soft-gold)" stroke-width="1.2"/>
    <line x1="130" y1="250" x2="310" y2="250" stroke="var(--soft-gold)" stroke-width="1.2"/>
    <circle cx="220" cy="250" r="3.5" fill="var(--soft-gold)"/>
    <circle cx="210" cy="250" r="2" fill="var(--soft-gold)"/>
    <circle cx="230" cy="250" r="2" fill="var(--soft-gold)"/>
    <line x1="180" y1="372" x2="260" y2="372" stroke="var(--soft-gold)" stroke-width="1"/>
    <circle cx="220" cy="372" r="2.5" fill="var(--soft-gold)"/>
  </svg>
  <div class="label-text label-brand">ORVALE</div>
  <div class="label-text label-range">COLLECTIONS</div>
  <div class="label-flourish" role="img" aria-label="Small calligraphic flourish"></div>
  <p class="label-text label-promise">Quality Essential Oils<br>&amp; Fragrances</p>
  <p class="label-text label-origin">100% Soy Wax<br>Handmade in Australia</p>
</section>

</body>
</html>
```